Zombie Themed Web Site Design

I am looking for a web page design for a web site that will be selling zombie themed items.

Starting out we are selling one product, a zombie combat patch so I would like the web design to be based of it, but the attached image should only be a starting point. Please do not hesitate to be as creative as possible.

The site design should be family friendly but defiantly be zombie themed. For the color schema it does not have to be the black and reds that the patch is based on for the page theme.

The Home page should be a page of shear zombie awesomeness that points to the products.

That other pages that are to be static, are the:
About Us, Gallery, Refund Policy, Privacy Policy, Terms & Conditions, Shipping and Delivery and Contact us pages.

-LINK- to the web site (there is nothing there yet)
http://ghoulbrigadegear.example

-LINK- to the zombie patch image
https://files.quillnest.example/s/k7m2p9q4r1t8vwx/Zombie.jpg

PSD file output is just fine, HTML and CSS files are even better.

If there are any questions, please leave a comment.
Updates

From the submission that I have been receiving, I need to clarifyjust what I am looking for. The theme of the site should be less of zombies risingout of the grave and eating people’s brains, and more a group of peoplethat have formed together (a “task force” if that helps) to hunt and kill zombies.I hope that this helps.

-Marcus    

Industry/Entity Type

Shipping

Requirements
Nice to have
• The use of a military font in the design would awsome.

```html
<!DOCTYPE html>
<html lang="en">
<head>
<meta charset="utf-8">
<title>Ghoul Brigade Gear</title>
<link rel="stylesheet" href="https://fonts.googleapis.com/css2?family=Black+Ops+One&family=Creepster&family=PT+Sans:wght@400;700&family=Open+Sans:wght@400&family=Tinos&display=swap">
<style>
  :root {
    --night: #000000;
    --sky-top: #3a3d44;
    --sky-mid: #5b6068;
    --grass: #4f6a2e;
    --header-top: #24362a;
    --header-bottom: #070b08;
    --logo: #7c9a78;
    --nav: #6e0f0f;
    --white: #ffffff;
    --body-copy: #f2f2f2;
    --feature-head: #e8e8e8;
    --feature-copy: #8d92b8;
    --button: #4b6b56;
    --button-text: #f0f0f0;
    --footer: #d01010;
    --hands-a: #4d6672;
    --hands-b: #1d2a30;
  }
  * { box-sizing: border-box; margin: 0; padding: 0; }
  html, body { width: 1200px; height: 610px; overflow: hidden; background: var(--night); }
  .canvas { position: relative; width: 1200px; height: 610px; overflow: hidden; }
  .backdrop {
    position: absolute; inset: 0;
    background:
      linear-gradient(to bottom, transparent 70%, var(--grass) 100%),
      radial-gradient(ellipse at 85% 15%, #8a8e96 0%, transparent 45%),
      linear-gradient(to bottom, var(--sky-top), var(--sky-mid) 60%, #3c4138);
  }
  .page {
    position: absolute; left: 242px; top: 2px; width: 714px; height: 574px;
    background: var(--night);
    box-shadow: 0 0 18px rgba(0,0,0,.7);
  }
  .site-header {
    height: 48px; display: flex; align-items: center; justify-content: space-between;
    padding: 0 10px 0 32px;
    background: linear-gradient(to bottom, var(--header-top), var(--header-bottom));
  }
  .brand {
    font-family: "PT Sans", sans-serif; font-weight: 700; font-size: 30px;
    color: var(--logo); letter-spacing: .5px;
  }
  .main-nav { display: flex; gap: 22px; }
  .main-nav a {
    font-family: "Black Ops One", sans-serif; font-size: 13px; color: var(--nav);
    text-decoration: none; letter-spacing: 1.5px; text-transform: lowercase;
  }
  .banner-title {
    position: absolute; left: 64px; top: 106px;
    font-family: "Creepster", cursive; font-size: 34px; font-weight: 400;
    color: var(--white); letter-spacing: 1px;
  }
  .banner-copy {
    position: absolute; left: 64px; top: 166px; width: 222px;
    font-family: "Open Sans", sans-serif; font-size: 11.2px; line-height: 19px;
    color: var(--body-copy);
  }
  .banner-art {
    position: absolute; left: 448px; top: 184px; width: 266px; height: 224px;
    background: radial-gradient(ellipse at 75% 45%, var(--hands-a) 0%, var(--hands-b) 55%, transparent 75%);
  }
  .features { position: absolute; left: 15px; top: 444px; display: flex; gap: 32px; }
  .feature { width: 178px; }
  .feature-title {
    font-family: "Black Ops One", sans-serif; font-weight: 400; font-size: 10px; line-height: 11px;
    color: var(--feature-head); letter-spacing: 1px;
  }
  .feature-copy {
    margin-top: 0; font-family: "Open Sans", sans-serif; font-size: 7.6px; line-height: 9px;
    color: var(--feature-copy);
  }
  .button {
    display: inline-block; margin: 5px 0 0 6px; width: 80px; height: 18px; line-height: 18px;
    text-align: center; border-radius: 2px; background: var(--button);
    font-family: "Black Ops One", sans-serif; font-size: 8px; color: var(--button-text);
    text-decoration: none;
  }
  .site-footer {
    position: absolute; left: 0; right: 0; top: 556px; text-align: center;
    font-family: "Tinos", serif; font-size: 9.5px; color: var(--footer);
  }
</style>
</head>
<body>
<div class="canvas">
  <div class="backdrop" role="img" aria-label="Foggy graveyard at dusk with headstones, grass and a lone figure in the mist"></div>
  <div class="page">
    <header class="site-header">
      <div class="brand">Ghoul Brigade</div>
      <nav class="main-nav">
        <a href="#">home</a>
        <a href="#">projects</a>
        <a href="#">about us</a>
        <a href="#">contact</a>
      </nav>
    </header>

    <h1 class="banner-title">BANNER TITLE</h1>
    <p class="banner-copy">Holiday waiter erudite headmaster movember Reginald pomfrey don't panic, cuthbert fennick Reginald pomfrey villain rupert danvers erudite headmaster sir grimsby gloom holiday waiter movember don't panic? Monty fairweather nefarious comb holiday waiter brandy knavish rogue, brandy toothbrush lady magnets musketeer stiff upper lip comb knavish rogue testosterone trophy nefarious monty fairweather holiday waiter?</p>
    <div class="banner-art" role="img" aria-label="Crowd of pale zombie arms reaching out from the right edge"></div>

    <section class="features">
      <article class="feature">
        <h2 class="feature-title">Quality Items</h2>
        <p class="feature-copy">Lorem ipsum dolor sit amet, consectetur adipisicing elit, sed do eiusmod tempor incididunt ut labore et dolore magna aliqua. Ut enim ad minim veniam, quis nostrud exercitation ullamco laboris nisi ut aliquip ex ea commodo consequat.</p>
        <a class="button" href="#">Learn More...</a>
      </article>
      <article class="feature">
        <h2 class="feature-title">Fast Shipment</h2>
        <p class="feature-copy">Lorem ipsum dolor sit amet, consectetur adipisicing elit, sed do eiusmod tempor incididunt ut labore et dolore magna aliqua. Ut enim ad minim veniam, quis nostrud exercitation ullamco laboris nisi ut aliquip ex ea commodo consequat.</p>
        <a class="button" href="#">Learn More...</a>
      </article>
      <article class="feature">
        <h2 class="feature-title">Refunding</h2>
        <p class="feature-copy">Lorem ipsum dolor sit amet, consectetur adipisicing elit, sed do eiusmod tempor incididunt ut labore et dolore magna aliqua. Ut enim ad minim veniam, quis nostrud exercitation ullamco laboris nisi ut aliquip ex ea commodo consequat.</p>
        <a class="button" href="#">Learn More...</a>
      </article>
    </section>

    <footer class="site-footer">© 2013 by Ghoul Brigade Gear. All rights reserved.</footer>
  </div>
</div>
</body>
</html>
```